Naturopath specialising in Children's Health

I have just started working in a new clinic where I will be predominantly treating children so I would like to rebrand with a business card that reflects this.

I would like a clever design which is subtly playful and will attract children and parents alike, while maintaining a professional look. It must also reflect that I utilize natural medicine - including herbal medicine and nutrition as part of my treatment. Employing the use of a plant or herb would be ideal. I had envisioned the image of a dandelion blowing in the wind (or being blown by a child) as a great combination of the playful yet natural medicine I am trying to ecompass in the card.

I would like to use yellow, orange, blue or green as the dominant colour for the card.

The front of the card should contain the logo and the words 'Maribel Stroud - Naturopath.'

The back of the card should contain the following details:
Maribel Stroud BHSc Nat, Dip RM
Naturopath, Herbalist, Nutritionist, Iridologist, Remedial Massage Therapist, Reiki Practitioner
0413 927 186
Willowfern Haven - (02) 9731 4068
maribel.stroud@kestrelmail.example
NHPA 81347

Industry/Entity Type

Clinic

```html
<!DOCTYPE html>
<html lang="en">
<head>
<meta charset="utf-8">
<title>Maribel Stroud – Naturopath Business Card</title>
<link rel="stylesheet" href="https://fonts.googleapis.com/css2?family=Josefin+Sans:wght@400;600&family=Merriweather:wght@400;700&display=swap">
<style>
  :root {
    --backdrop: #e9e7e2;
    --forest-deep: #0d6b2a;
    --forest: #138c34;
    --forest-glow: #6fd13f;
    --lime: #8fd928;
    --ink: #111a0c;
    --paper: #ffffff;
  }
  * { margin: 0; padding: 0; box-sizing: border-box; }
  html, body {
    width: 1200px;
    height: 1000px;
    overflow: hidden;
    background: var(--backdrop);
  }
  .canvas {
    position: relative;
    width: 1200px;
    height: 1000px;
  }
  .card {
    position: absolute;
    left: 282px;
    width: 678px;
    height: 392px;
    border-radius: 16px;
    overflow: hidden;
  }
  /* Front */
  .card--front {
    top: 70px;
    background:
      radial-gradient(circle at 82% 20%, var(--forest-glow) 0%, #3db33a 22%, var(--forest) 52%, var(--forest-deep) 100%);
  }
  .front__plant {
    position: absolute;
    left: 0;
    top: 0;
    width: 200px;
    height: 392px;
    background: linear-gradient(160deg, rgba(255,255,255,0.22) 0%, rgba(255,255,255,0.08) 60%, rgba(255,255,255,0.28) 100%);
  }
  .front__seeds {
    position: absolute;
    left: 200px;
    top: 18px;
    width: 430px;
    height: 150px;
    border-radius: 60px;
    background: radial-gradient(ellipse at center, rgba(255,255,255,0.14) 0%, rgba(255,255,255,0) 75%);
  }
  .front__title {
    position: absolute;
    left: 230px;
    top: 268px;
    width: 420px;
    text-align: center;
    color: var(--paper);
    font-family: "Josefin Sans", sans-serif;
  }
  .front__name {
    font-size: 46px;
    font-weight: 600;
    line-height: 1;
    letter-spacing: 0.5px;
    font-variant: small-caps;
    white-space: nowrap;
  }
  .front__role {
    margin-top: 14px;
    font-size: 25px;
    font-weight: 400;
    letter-spacing: 0.5px;
    text-transform: uppercase;
  }
  /* Back */
  .card--back {
    top: 497px;
    background: var(--lime);
    color: var(--ink);
    font-family: "Merriweather", serif;
  }
  .back__name {
    position: absolute;
    left: 25px;
    top: 31px;
    font-size: 25px;
    font-weight: 700;
    line-height: 1.2;
  }
  .back__credentials {
    position: absolute;
    left: 25px;
    top: 67px;
    font-size: 16px;
    line-height: 1.3;
  }
  .back__services {
    position: absolute;
    left: 25px;
    top: 101px;
    font-size: 14px;
    line-height: 22px;
  }
  .back__divider {
    position: absolute;
    left: 5px;
    right: 13px;
    top: 273px;
    border-top: 2px dotted rgba(17,26,12,0.6);
  }
  .back__contact {
    position: absolute;
    right: 27px;
    top: 284px;
    text-align: right;
    font-size: 14px;
    line-height: 21.5px;
    list-style: none;
  }
</style>
</head>
<body>
<main class="canvas">
  <section class="card card--front" aria-label="Card front">
    <div class="front__plant" role="img" aria-label="Illustration of dandelion clocks on long stems with jagged leaves"></div>
    <div class="front__seeds" role="img" aria-label="Dandelion seeds drifting on the wind"></div>
    <div class="front__title">
      <h1 class="front__name">Maribel Stroud</h1>
      <p class="front__role">Naturopath</p>
    </div>
  </section>

  <section class="card card--back" aria-label="Card back">
    <h2 class="back__name">Maribel Stroud</h2>
    <p class="back__credentials">BHSc Nat, Dip RM</p>
    <p class="back__services">Naturopath, Herbalist, Nutritionist, Iridologist,<br>Remedial Massage Therapist, Reiki Practitioner</p>
    <div class="back__divider"></div>
    <ul class="back__contact">
      <li>0413 927 186</li>
      <li>Willowfern Haven - (02) 9731 4068</li>
      <li>maribel.stroud@kestrelmail.example</li>
      <li>NHPA 81347</li>
    </ul>
  </section>
</main>
</body>
</html>
```